Tots at Play

We need a logo and graphich design for a one page text for our Tots @play program, it would nened to match or be inspired from our corporate indentity which can be seen at www.halvora-partners.com

Dear XXX
BRT is proud to launch its first ever TOTS @ PLAY day! We invite you and your child(ren) to join us on this special day, and strengthen the connection between education and work, and your relationship between parent and child(ren).

Who? All children, all ages
Where? BRT offices
When? January 29th, from 13h – 17h

Tots @ Play is the perfect time to start shaping your children’s future through education and experience at BRT with a program tailored to target each age group. There will be group activities and sessions, as well as one on one time for parents and their children.
We are excited to work together with you and your children to create a true sense of community, and celebrate the opportunities and possibilities for the next generation. It’s a day to share your passion and know-how and show what happens when you are at work. We will show children the value of education and help them discover the power and potential of a balanced work and family life. We would like to give you and your children an opportunity to express their future goals and dreams and help begin together the steps towards achieving these through the follow up with Tots @ Quest. BRT is developing a multi-program to enable parents and children to realize the future they dream of.
We look forward to seeing you @ Work!

Industry/Entity Type

Education

```html
<!DOCTYPE html>
<html lang="en">
<head>
<meta charset="utf-8">
<title>Tots @ Play – Invitation Letter</title>
<link rel="stylesheet" href="https://fonts.googleapis.com/css2?family=Delius&display=swap">
<style>
  :root {
    --ink-purple: #a33bb5;
    --ink-magenta: #e0249a;
    --band: #b04fc6;
    --paper: #ffffff;
    --art-warm: #f6d9a8;
    --art-cool: #f4a9c9;
  }
  * { margin: 0; padding: 0; box-sizing: border-box; }
  html, body {
    width: 929px; height: 1200px; overflow: hidden; background: var(--paper);
  }
  .letter {
    position: relative; width: 929px; height: 1200px; overflow: hidden;
    background: var(--paper);
    font-family: "Delius", "Comic Neue", sans-serif;
    color: var(--ink-purple);
  }
  .side-band {
    position: absolute; top: 0; right: 0; width: 100px; height: 1200px;
    background: var(--band);
  }

  .brand-name {
    position: absolute; right: 150px; top: 120px;
    font-size: 62px; line-height: 1; color: var(--ink-purple);
  }

  .content {
    position: absolute; left: 110px; top: 200px; width: 676px;
    font-size: 20px; line-height: 28px;
  }
  .wrap-spacer { float: right; width: 0; height: 645px; }
  .art-gap { float: right; clear: right; width: 250px; height: 220px; }
  .salutation { margin-bottom: 28px; }
  .content p { text-align: justify; }
  .intro { margin-bottom: 28px; }
  .facts { list-style: none; color: var(--ink-magenta); margin-bottom: 28px; }
  .closing { margin-top: 28px; }

  .kids-art {
    position: absolute; left: 548px; top: 858px; width: 268px; height: 300px;
    border-radius: 24px 24px 8px 8px;
    background: linear-gradient(180deg, var(--art-warm) 0%, var(--art-cool) 100%);
  }
</style>
</head>
<body>
<main class="letter">
  <div class="side-band" aria-hidden="true"></div>

  <header class="brand-name">BRT</header>

  <section class="content">
    <div class="wrap-spacer"></div>
    <div class="art-gap"></div>
    <p class="salutation">Dear XXX</p>
    <p class="intro">BRT is proud to launch its first ever TOTS @ PLAY day! We invite you and your child(ren) to join us on this special day, and strengthen the connection between education and work, and your relationship between parent and child(ren).</p>
    <ul class="facts">
      <li>Who? All children, all ages</li>
      <li>Where? BRT offices</li>
      <li>When? January 29th, from 13h – 17h</li>
    </ul>
    <p>Tots @ Play is the perfect time to start shaping your children’s future through education and experience at BRT with a program tailored to target each age group. There will be group activities and sessions, as well as one on one time for parents and their children.</p>
    <p>We are excited to work together with you and your children to create a true sense of community, and celebrate the opportunities and possibilities for the next generation. It’s a day to share your passion and know-how and show what happens when you are at work. We will show children the value of education and help them discover the power and potential of a balanced work and family life. We would like to give you and your children an opportunity to express their future goals and dreams and help begin together the steps towards achieving these through the follow up with Tots @ Quest. BRT is developing a multi-program to enable parents and children to realize the future they dream of.</p>
    <p class="closing">We look forward to seeing you @ Work!</p>
  </section>

  <div class="kids-art" role="img" aria-label="Illustration of two children holding a Tots @ Play banner"></div>
</main>
</body>
</html>
```